ARC VOLLEY Business Card Project

I'd like to request a business card design for the new company I've launched.
The name of the company is "ARC VOLLEY" an indoor unmanned tennis practice facility.
We would like to see designs that use our brand identity color in the logo I've attached.
We hope to get the design with modern, luxurious and elegant tone and manner.
We hope the logo should not be too big.

Business card must have elements as below:
- Logo (One of the logos I've attached)
- Name (In Korean Text) : 박 서 윤
- Title (In Korean Text) : 대표
- Phone Number : 010-8472-3916
- Email Address : seoyun.park@arcvolley-example.co.kr
- Website : www.arcvolley-example.co.kr
- Instagram : arcvolley
- Address (In Korean text) : 경기도 용인시 수지구 풍덕천로 456 미래타워 5층 501호, 502호

Target Market(s)

Tennis amateurs in 20 to 40s

Industry/Entity Type

Sports, Hobby

Contact Information for Business Card

- Logo (One of the logos I've attached) - Name (In Korean Text) : 박 서 윤 - Title (In Korean Text) : 대표 - Phone Number : 010-8472-3916 - Email Address : seoyun.park@arcvolley-example.co.kr - Website : www.arcvolley-example.co.kr - Instagram : arcvolley - Address (In Korean text) : 경기도 용인시 수지구 풍덕천로 456 미래타워 5층 501호, 502호

Font styles to use
Sans Serif

Requirements
Must have
• Double sided
Nice to have
• Logo with intaglio or relief embossing
Should not have
• Logo should not be too big.

```html
<!DOCTYPE html>
<html lang="ko">
<head>
<meta charset="utf-8">
<title>ARC VOLLEY Business Card</title>
<link href="https://fonts.googleapis.com/css2?family=Cinzel:wght@400;600&family=Noto+Sans+KR:wght@400;700&display=swap" rel="stylesheet">
<style>
  :root {
    --brand-green: #2d5138;
    --accent-grey: #8a8b8e;
    --card-white: #ffffff;
    --ink: #1a1a1a;
    --backdrop: #262626;
  }
  * { margin: 0; padding: 0; box-sizing: border-box; }
  html, body { width: 1200px; height: 780px; overflow: hidden; }
  body {
    background: var(--backdrop);
    position: relative;
  }
  .card {
    position: absolute;
    width: 560px;
    height: 311px;
    top: 234px;
    overflow: hidden;
  }
  .card--front { left: 25px; background: var(--brand-green); }
  .card--back { left: 615px; background: var(--card-white); }

  /* front */
  .front-brand {
    position: absolute;
    inset: 0;
    display: flex;
    flex-direction: column;
    align-items: center;
    justify-content: center;
    gap: 18px;
  }
  .front-brand__mark {
    width: 70px; height: 70px;
    border-radius: 50%;
    background: var(--card-white);
  }
  .front-brand__name {
    font-family: 'Cinzel', serif;
    font-weight: 400;
    font-size: 40px;
    letter-spacing: 1px;
    color: var(--card-white);
  }

  /* back */
  .swoosh { position: absolute; left: 0; top: 0; }
  .back-brand {
    position: absolute;
    left: 24px; top: 30px;
    display: flex; align-items: center; gap: 10px;
  }
  .back-brand__mark {
    width: 40px; height: 40px; border-radius: 50%;
    background: var(--brand-green);
  }
  .back-brand__name {
    font-family: 'Cinzel', serif;
    font-weight: 400;
    font-size: 22px;
    color: var(--brand-green);
  }
  .rule { position: absolute; height: 1px; background: var(--ink); }
  .rule--top { left: 150px; top: 96px; width: 340px; }
  .rule--address { left: 24px; top: 140px; width: 290px; }
  .name-bar {
    position: absolute; right: 0; top: 22px;
    width: 14px; height: 66px;
    background: var(--accent-grey);
  }
  .person-name {
    position: absolute; right: 40px; top: 26px;
    font-family: 'Noto Sans KR', sans-serif;
    font-weight: 700;
    font-size: 32px;
    color: var(--brand-green);
    letter-spacing: 2px;
  }
  .person-title {
    position: absolute; right: 36px; top: 82px;
    font-family: 'Noto Sans KR', sans-serif;
    font-weight: 400;
    font-size: 15px;
    color: var(--ink);
  }
  .address {
    position: absolute; left: 24px; top: 148px;
    font-family: 'Noto Sans KR', sans-serif;
    font-weight: 700;
    font-size: 14px;
    line-height: 21px;
    color: var(--ink);
  }
  .contacts {
    position: absolute; left: 36px; top: 198px;
    list-style: none;
    font-family: 'Cinzel', serif;
    font-size: 10.5px;
    color: var(--ink);
  }
  .contacts li { display: flex; align-items: center; gap: 8px; height: 17px; white-space: nowrap; }
  .contacts svg { width: 11px; height: 11px; flex: none; }
</style>
</head>
<body>
  <section class="card card--front">
    <div class="front-brand">
      <div class="front-brand__mark"></div>
      <div class="front-brand__name">ARC VOLLEY</div>
    </div>
  </section>

  <section class="card card--back">
    <svg class="swoosh" width="560" height="311" viewBox="0 0 560 311" aria-hidden="true">
      <path d="M170 311 Q380 290 560 160 L560 174 Q400 250 280 311 Z" fill="var(--accent-grey)"/>
      <path d="M296 311 Q410 256 560 184 L560 311 Z" fill="var(--brand-green)"/>
    </svg>

    <div class="back-brand">
      <div class="back-brand__mark"></div>
      <div class="back-brand__name">ARC VOLLEY</div>
    </div>

    <div class="name-bar"></div>
    <div class="person-name">박 서 윤</div>
    <div class="rule rule--top"></div>
    <div class="person-title">대표</div>

    <div class="rule rule--address"></div>
    <p class="address">경기도 용인시 수지구 풍덕천로<br>456 미래타워 5층 501호, 502호</p>

    <ul class="contacts">
      <li>
        <svg viewBox="0 0 12 12"><path d="M2.5 1 L4.5 1 L5.2 3.5 L4 4.5 Q5 6.8 7.5 8 L8.5 6.8 L11 7.5 L11 9.5 Q10.5 11 9 11 Q1 10 1 2.5 Q1 1 2.5 1 Z" fill="var(--brand-green)"/></svg>
        010-8472-3916
      </li>
      <li>
        <svg viewBox="0 0 12 12"><circle cx="6" cy="6" r="5.5" fill="var(--brand-green)"/></svg>
        ARCVOLLEY
      </li>
      <li>
        <svg viewBox="0 0 12 12"><circle cx="6" cy="6" r="5" fill="none" stroke="var(--brand-green)" stroke-width="1.2"/><ellipse cx="6" cy="6" rx="2.2" ry="5" fill="none" stroke="var(--brand-green)" stroke-width="1"/><line x1="1" y1="6" x2="11" y2="6" stroke="var(--brand-green)" stroke-width="1"/></svg>
        WWW.ARCVOLLEY-EXAMPLE.CO.KR
      </li>
      <li>
        <svg viewBox="0 0 12 12"><rect x="0.8" y="2.5" width="10.4" height="7.5" fill="none" stroke="var(--brand-green)" stroke-width="1.2"/><path d="M0.8 2.5 L6 6.8 L11.2 2.5" fill="none" stroke="var(--brand-green)" stroke-width="1.2"/></svg>
        SEOYUN.PARK@ARCVOLLEY-EXAMPLE.CO.KR
      </li>
    </ul>
  </section>
</body>
</html>
```